Stress Fracture Infographic for Scientific Paper

We need an infographic for a research/scientific paper. We would like the infographic to give readers a clear and eye-catching overview about the factors that put athletes and military personnel at risk for stress fractures. The design needs to communicate that the risk factors are cumulative and interactive; however, how they specifically accumulate and interact has not been studied or shown in the literature (we need healthcare providers who subjectively assess cumulative risk profiles in athletes and we concurrently need scientists to evaluate the interdependence of risk factors). We define cumulative risk profile as: a subjective clinical determination of the number of factors putting an athlete at risk along with thoughtful consideration regarding how all the risk factors interact with one another. We would like the infographic to display this cumulative risk profile idea.

The risk factors can be categorized as:
INTRINSIC-
Non-modifiable (such as sex, race, age, genetics, anatomical structure, and prior bone stress injury), modifiable (muscle strength, muscle fatigue, flexibility, biomechanics, stress, recovery strategies, nutrition, energy deficiency), unclear if modifiable, not, or somewhere in between (such as gut health);

EXTRINSIC-
Modifiable (footwear, training surface, workload)

Target Market(s)

Researchers and clinicians

Requirements
Must have
• A scientific feel
Nice to have
• Creative way to display the cumulative and interactive impact of risk factors
Should not have
• Too cartoon-ish or child-like feel

```html
<!DOCTYPE html>
<html lang="en">
<head>
<meta charset="utf-8">
<title>Factors of Risk for Stress Fractures</title>
<link href="https://fonts.googleapis.com/css2?family=Montserrat:wght@500;600;700&family=Russo+One&display=swap" rel="stylesheet">
<style>
  :root {
    --bg: #ffffff;
    --sky: #bde6f7;
    --glow: #ffbb88;
    --ink: #454545;
    --rule: #8f8f8f;
    --blue: #0a6ab8;
    --square: #4a9ad4;
    --badge: #7f7f7f;
    --orange: #f5822a;
    --title-grey: #7a7a7a;
  }
  * { margin: 0; padding: 0; box-sizing: border-box; }
  html, body { width: 1200px; height: 1200px; overflow: hidden; background: var(--bg); }
  body { font-family: "Montserrat", Arial, sans-serif; color: var(--ink); }
  .canvas { position: relative; width: 1200px; height: 1200px; }

  .risk-disc {
    position: absolute; left: 286px; top: 219px; width: 623px; height: 623px; border-radius: 50%;
    background: radial-gradient(circle at 41% 68%, var(--glow) 0%, #f6cdaf 18%, #e2dcd4 34%, var(--sky) 52%, var(--sky) 100%);
  }
  .runner-figure {
    position: absolute; left: 431px; top: 512px; width: 275px; height: 326px;
    background: radial-gradient(ellipse at 50% 45%, rgba(255,255,255,0.95) 0%, rgba(255,255,255,0.75) 40%, rgba(255,255,255,0) 72%);
  }

  .heading { position: absolute; font-weight: 700; font-size: 25px; line-height: 1; top: 221px; white-space: nowrap; }
  .heading--intrinsic { right: 664px; }
  .heading--extrinsic { left: 561px; }
  .divider { position: absolute; left: 552px; top: 216px; width: 1px; height: 210px; background: var(--rule); }
  .divider--joint { left: 563px; top: 428px; height: 148px; }

  .factor-group { position: absolute; }
  .factor-group h3 { font-weight: 700; font-size: 19px; line-height: 22px; white-space: nowrap; }
  .factor-list { list-style: none; border-top: 1px solid var(--rule); }
  .factor-list li {
    font-weight: 600; font-size: 14px; height: 21.7px; line-height: 21px; white-space: nowrap;
    border-bottom: 1px solid var(--rule);
  }
  .factor-group--nonmod { left: 329px; top: 250px; width: 207px; text-align: right; }
  .factor-group--intrinsic-mod { left: 329px; top: 418px; width: 208px; text-align: right; }
  .factor-group--intrinsic-mod h3 { padding-left: 82px; }
  .factor-group--extrinsic { left: 562px; top: 250px; width: 208px; }

  .link-square { position: absolute; left: 547px; top: 412px; width: 14px; height: 13px; background: var(--square); }
  .link-line { position: absolute; height: 1px; background: var(--rule); }

  .unclear-badge {
    position: absolute; left: 289px; top: 431px; width: 120px; height: 120px; border-radius: 50%;
    background: var(--badge); color: #fff; text-align: center;
  }
  .unclear-badge .badge-title { font-weight: 700; font-size: 16px; line-height: 19px; margin-top: 27px; }
  .unclear-badge .badge-rule { height: 1px; background: rgba(255,255,255,0.6); margin-top: 6px; }
  .unclear-badge .badge-item { font-weight: 500; font-size: 15px; margin-top: 6px; }

  .cumulative { position: absolute; left: 577px; top: 370px; width: 300px; color: var(--blue); }
  .cumulative h2 { font-weight: 700; font-size: 19px; line-height: 24px; white-space: nowrap; }
  .cumulative p { font-weight: 500; font-size: 11.6px; line-height: 15px; margin-top: 5px; }

  .title-block { position: absolute; left: 648px; top: 524px; width: 223px; text-align: center; font-family: "Russo One", "Arial Black", sans-serif; }
  .title-rule { position: absolute; left: 0; width: 223px; height: 1px; background: var(--rule); }
  .title-lead { position: absolute; left: 0; width: 223px; top: 0; color: var(--title-grey); font-size: 26px; line-height: 28px; padding-top: 1px; letter-spacing: 1px; }
  .title-key { position: absolute; left: 0; width: 223px; color: var(--orange); font-size: 41px; line-height: 40px; white-space: nowrap; }
</style>
</head>
<body>
<main class="canvas">
  <div class="risk-disc"></div>
  <div class="runner-figure" role="img" aria-label="Silhouette of a running athlete with highlighted stress fracture sites along the hip, leg and foot"></div>

  <h1 class="heading heading--intrinsic">Intrinsic Factors</h1>
  <h1 class="heading heading--extrinsic">Extrinsic Factors</h1>
  <div class="divider"></div>
  <div class="divider divider--joint"></div>

  <section class="factor-group factor-group--nonmod">
    <h3>Non-modifiable</h3>
    <ul class="factor-list">
      <li>Sex</li><li>Race</li><li>Age</li><li>Genetics</li><li>Anatomical structure</li><li>Prior bone stress injury</li>
    </ul>
  </section>

  <section class="factor-group factor-group--intrinsic-mod">
    <h3>Modifiable</h3>
    <ul class="factor-list">
      <li>Muscle strength</li><li>Muscle fatigue</li><li>Flexibility</li><li>Biomechanics</li><li>Stress</li><li>Recovery strategies</li><li>Nutrition</li><li>Energy deficiency</li>
    </ul>
  </section>

  <section class="factor-group factor-group--extrinsic">
    <h3>Modifiable</h3>
    <ul class="factor-list">
      <li>Footwear</li><li>Training Surface</li><li>Workload</li>
    </ul>
  </section>

  <div class="link-line" style="left:411px; top:414px; width:152px;"></div>
  <div class="link-line" style="left:544px; top:428px; width:143px;"></div>
  <div class="link-square"></div>

  <div class="unclear-badge">
    <div class="badge-title">Unclear if<br>Modifiable</div>
    <div class="badge-rule"></div>
    <div class="badge-item">Gut Health</div>
  </div>

  <section class="cumulative">
    <h2>Cumulative Stress Factor</h2>
    <p>We define cumulative risk profile as: a subjective clinical determination of the number of factors putting an athlete at risk along with thoughtful consideration regarding how all the risk factors interact with one another.</p>
  </section>

  <section class="title-block">
    <div class="title-rule" style="top:0;"></div>
    <div class="title-lead">Factors of<br>Risk for</div>
    <div class="title-rule" style="top:58px;"></div>
    <div class="title-key" style="top:56px;">Stress</div>
    <div class="title-rule" style="top:97px;"></div>
    <div class="title-key" style="top:96px; left:-6px; width:235px;">Fractures</div>
    <div class="title-rule" style="top:137px;"></div>
  </section>
</main>
</body>
</html>
```